Brightwell Bonds and Households Initiative

We need a flyer that invites low-income Spanish speaking individuals to our program. The program is 12 weeks. We offer healthy relationship education, and financial stability. We also touch on workforce development. These workshops are for couples only.

We are in five locations, so we need a flyer that we can change the text to be able to update the address, dates and any additional information based on our needs.

Attached is the logo we would like to use. I have also attached a previous flyer that we created to give you an idea of the text that is included.

Target Market(s)

We are reaching out to low income adult couples

Font styles to use
Serif

Requirements
Must have
• This flyer must catch the eye of couples wanting to improve their relationship, and finances.
Nice to have
• Some space for us to plug in dates location and times. This flyer also has to have our funding statement at the bottom.

```html
<!DOCTYPE html>
<html lang="es">
<head>
<meta charset="utf-8">
<title>Talleres Para Parejas</title>
<link href="https://fonts.googleapis.com/css2?family=Roboto+Condensed:ital,wght@0,400;1,700&family=Didact+Gothic&family=Source+Sans+3:wght@400;600;700&display=swap" rel="stylesheet">
<style>
  :root {
    --navy: #10305a;
    --navy-dark: #0f2b55;
    --orange: #ef8a1c;
    --orange-band: #ec7f14;
    --ink: #1d1d1f;
    --backdrop: #3b3b3c;
    --sky: #dfe9f3;
  }
  * { margin: 0; padding: 0; box-sizing: border-box; }
  html, body { width: 1200px; height: 1200px; overflow: hidden; background: var(--backdrop); }
  .flyer {
    position: absolute; left: 189px; top: 20px; width: 821px; height: 1160px; overflow: hidden;
    background: linear-gradient(180deg, #ffffff 0%, #ffffff 16%, var(--sky) 30%, #eef3f8 45%, #ffffff 60%, #ffffff 100%);
    font-family: "Source Sans 3", sans-serif; color: var(--ink);
  }
  .abs { position: absolute; }
  .center { left: 0; width: 100%; text-align: center; }
  .program-name { top: 100px; font-family: "Source Sans 3", sans-serif; font-weight: 600; font-size: 23px; color: var(--orange); }
  .program-focus { top: 132px; font-family: "Source Sans 3", sans-serif; font-size: 13px; color: var(--navy); }
  .title { top: 168px; font-family: "Roboto Condensed", sans-serif; font-style: italic; font-weight: 700; font-size: 86px; line-height: 96px; color: var(--navy); letter-spacing: -0.5px; }
  .slogan { top: 266px; font-family: "Didact Gothic", sans-serif; font-size: 36px; line-height: 43px; color: var(--orange); }
  .schedule { top: 362px; left: 0; width: 100%; }
  .schedule .col { position: absolute; top: 0; }
  .schedule .dates { right: 432px; text-align: right; }
  .schedule .hours { left: 435px; }
  .schedule .divider { position: absolute; left: 411px; top: 4px; width: 2px; height: 56px; background: var(--ink); }
  .label { font-family: "Roboto Condensed", sans-serif; font-size: 23px; line-height: 28px; color: var(--ink); }
  .value { font-weight: 700; font-size: 23px; line-height: 30px; color: var(--navy); }
  .location { top: 442px; }
  .location .addr { font-weight: 600; font-size: 20px; line-height: 25px; color: var(--navy); }
  .note { top: 557px; left: 124px; font-family: "Didact Gothic", sans-serif; font-size: 26px; color: var(--ink); }
  .photo {
    top: 600px; left: 260px; width: 561px; height: 465px;
    background: radial-gradient(ellipse closest-side at 62% 55%, #b98a6a 0%, #8f6c5a 35%, #6d7d95 62%, rgba(200,205,215,0.55) 85%, rgba(255,255,255,0) 100%);
  }
  .register { top: 663px; left: 0; width: 456px; height: 89px; background: var(--orange-band); color: #fff; padding: 9px 0 0 25px; }
  .register .head { font-weight: 700; font-size: 18.5px; line-height: 22px; }
  .register .info { font-size: 15px; line-height: 20px; margin-top: 5px; }
  .register svg { vertical-align: -2px; margin: 0 4px 0 10px; }
  .topics { top: 765px; left: 24px; width: 300px; }
  .topics h2 { font-family: "Didact Gothic", sans-serif; font-weight: 400; font-size: 23px; line-height: 28px; color: var(--ink); margin-bottom: 6px; }
  .topics li { list-style: none; position: relative; padding-left: 25px; font-size: 15.5px; line-height: 19px; margin-bottom: 12px; }
  .topics li svg { position: absolute; left: 0; top: 3px; }
  .footer { top: 1065px; left: 0; width: 100%; height: 95px; background: var(--navy-dark); }
  .funding { position: absolute; left: 26px; top: 16px; width: 500px; color: #fff; font-size: 11px; line-height: 15px; text-align: justify; }
  .partner { position: absolute; background: #fff; display: flex; align-items: center; justify-content: center; text-align: center; font-weight: 700; font-size: 10px; line-height: 12px; color: var(--navy); padding: 4px; }
  .partner.one { left: 558px; top: 10px; width: 114px; height: 58px; }
  .partner.two { left: 703px; top: 16px; width: 98px; height: 50px; }
</style>
</head>
<body>
<main class="flyer">
  <div class="abs center program-name">Brightwell Bonds and Households Initiative</div>
  <div class="abs center program-focus">Educación en relaciones sanas, estabilidad financiera y desarrollo laboral</div>

  <h1 class="abs center title">Talleres Para Parejas</h1>
  <p class="abs center slogan">Porque una relación sana esta<br>“A Nuestro Alcance”</p>

  <section class="abs schedule">
    <div class="col dates"><div class="label">Fecha de talleres</div><div class="value">Jueves Octubre 03, 12, 19, 26</div></div>
    <div class="divider"></div>
    <div class="col hours"><div class="label">Horario:</div><div class="value">5:30pm –8:00pm</div></div>
  </section>

  <section class="abs center location">
    <div class="label">Ubicación:</div>
    <div class="addr">Cedar Hollow Family Resource Center</div>
    <div class="addr">4870 Linden Ave, Fairhaven CA 90210</div>
    <div class="addr">(555) 014-2290</div>
  </section>

  <p class="abs note">*Cuidado de niños y cena será proporcionado</p>

  <div class="abs photo" role="img" aria-label="Fotografía de una pareja sonriente abrazada al aire libre con luz de atardecer"></div>

  <section class="abs register">
    <div class="head">Registración requerida Llámanos hoy!</div>
    <div class="info">Para más información llame a&nbsp; Cedar Hollow Family<br>Resource Center<svg width="13" height="13" viewBox="0 0 14 14"><circle cx="7" cy="7" r="6" fill="none" stroke="#fff" stroke-width="1.3"/><path d="M4.6 4.2c.4-.4.8-.3 1 .1l.5.9c.2.3.1.6-.2.8l-.3.2c.3.8.9 1.4 1.7 1.8l.2-.3c.2-.3.5-.4.8-.2l.9.5c.4.2.4.6.1 1-.6.7-1.3.8-2.2.3-1.2-.7-2.2-1.7-2.8-2.9-.4-.9-.3-1.6.3-2.2z" fill="#fff"/></svg>(555) 014-2291</div>
  </section>

  <section class="abs topics">
    <h2>Temas incluyen:</h2>
    <ul>
      <li><svg width="19" height="13" viewBox="0 0 19 13"><circle cx="6" cy="7.5" r="4.6" fill="none" stroke="#10305a" stroke-width="1.5"/><circle cx="12" cy="5.5" r="4.6" fill="none" stroke="#10305a" stroke-width="1.5"/></svg>Llaves para la buena&nbsp; communicación</li>
      <li><svg width="19" height="13" viewBox="0 0 19 13"><circle cx="6" cy="7.5" r="4.6" fill="none" stroke="#10305a" stroke-width="1.5"/><circle cx="12" cy="5.5" r="4.6" fill="none" stroke="#10305a" stroke-width="1.5"/></svg>Tipos de personalidad y expectativas</li>
      <li><svg width="19" height="13" viewBox="0 0 19 13"><circle cx="6" cy="7.5" r="4.6" fill="none" stroke="#10305a" stroke-width="1.5"/><circle cx="12" cy="5.5" r="4.6" fill="none" stroke="#10305a" stroke-width="1.5"/></svg>Señales de peligro en una relación</li>
      <li><svg width="19" height="13" viewBox="0 0 19 13"><circle cx="6" cy="7.5" r="4.6" fill="none" stroke="#10305a" stroke-width="1.5"/><circle cx="12" cy="5.5" r="4.6" fill="none" stroke="#10305a" stroke-width="1.5"/></svg>Técnicas para formar y&nbsp; sostener una<br>relación sana</li>
      <li><svg width="19" height="13" viewBox="0 0 19 13"><circle cx="6" cy="7.5" r="4.6" fill="none" stroke="#10305a" stroke-width="1.5"/><circle cx="12" cy="5.5" r="4.6" fill="none" stroke="#10305a" stroke-width="1.5"/></svg>Resolucion de problemas</li>
      <li><svg width="19" height="13" viewBox="0 0 19 13"><circle cx="6" cy="7.5" r="4.6" fill="none" stroke="#10305a" stroke-width="1.5"/><circle cx="12" cy="5.5" r="4.6" fill="none" stroke="#10305a" stroke-width="1.5"/></svg>Como mantener la diversion</li>
      <li><svg width="19" height="13" viewBox="0 0 19 13"><circle cx="6" cy="7.5" r="4.6" fill="none" stroke="#10305a" stroke-width="1.5"/><circle cx="12" cy="5.5" r="4.6" fill="none" stroke="#10305a" stroke-width="1.5"/></svg>Como adminstrar el dinero entre pareja Y<br>muchos mas</li>
    </ul>
  </section>

  <footer class="abs footer">
    <p class="funding">“Funding for this project was provided by the Northfield Department of Family Services, Office for Children and Households, Grant: #42BW7316. These services are avaiable to all eligible persons, regardless of race, gender, age, disability, or religion.”</p>
    <div class="partner one">Cedar Hollow Family Resource Center</div>
    <div class="partner two">Riverbend Community Alliance</div>
  </footer>
</main>
</body>
</html>
```